NU Staffing DL Flyer

Nu staffing needs a glossy brochure designed for an upcoming VIP event of our clients which are real estate agencies.

Background:
Nu Staffing specialises in Realestate recruitment in Australia. We have been in the Realestate Recruitment industry for 18 years and are the highest referred agency in the Brisbane Market. We Recruit Property Managers, Commercial and Residential, Sales and support staff for our clients.

Guideline:
- The flyer will be DL size (210x99mm)
- We would like to see designs that use the colors Green and Black same as our logo (attached)
- We would like something modern with a sleek corporate feel
- Need to include other information as detailed below in the "Must have" section
Updates

My logo and contact details is a must on the DHL flyer

Design is up to you

Kind Regards

Martin

Reason: Hi Designers Thank you for your help it is a very hard decision that is why I have made 1. prize $160 and 2. prize $100 and extended the deadline until Wednesday. Kind Regards Martin

Target Market(s)

Residential and Commercial Realestate firms in Australia

Industry/Entity Type

Real Estate

Requirements
Must have
• Why clients use NU:
With extensive years of recruitment experience we are the highest referred recruitment company in the Brisbane market.“Our clients benefit from our wealth of experience and knowledge within their industry to recruit the right candidate.”

- Why Candidates use NU:
“With our long standing experience within recruitment , we take the time and care attitude to find the right position and culture suityour working experience."

- Nu Logo
- Website details: www.nustaffing-example.com.au
- Contact details:
Martin Holroyd
Recruitment Manager
Mb: 0412 586 230
Ph: 3951 2407
Fax: 3951 2409
E: martin@nustaffing-example.com.au
Level 1/ 218 Wexcombe Street, Spring Hill QLD 4004
Nice to have
• - Why Nu does quality and background checks on candidates
- The advantage of using Nu Staffing vs Recruitment on your own
- 12 week Guarantee period on all placements

```html
<!DOCTYPE html>
<html lang="en">
<head>
<meta charset="utf-8">
<title>NU Staffing DL Flyer</title>
<link href="https://fonts.googleapis.com/css2?family=Roboto:ital,wght@0,300;0,400;0,700;1,300;1,400&display=swap" rel="stylesheet">
<style>
:root{
  --stage:#5b5b5d;
  --paper:#ffffff;
  --ink:#2b2b2b;
  --dark:#2e2f2d;
  --green:#5cbd3f;
  --green-deep:#2f7426;
  --text-light:#f2f2f2;
  --pattern:#3a3b39;
}
*{margin:0;padding:0;box-sizing:border-box}
html,body{width:1200px;height:800px;overflow:hidden}
body{background:var(--stage);font-family:"Roboto",Arial,sans-serif;position:relative}
.flyer{position:absolute;top:25px;width:353px;height:748px;background:var(--dark);box-shadow:0 4px 14px rgba(0,0,0,.45);overflow:hidden}
.flyer--front{left:217px}
.flyer--back{left:629px}
.header{position:absolute;left:0;top:0;width:100%;background:var(--paper);border-bottom:5px solid var(--green)}
.flyer--front .header{height:313px}
.flyer--back .header{height:210px}
.brand{position:absolute;left:0;top:48px;width:100%;display:flex;align-items:center;justify-content:center;gap:14px}
.brand__dot{width:54px;height:54px;border-radius:50%;background:var(--green)}
.brand__name{font-weight:700;font-size:46px;color:var(--green);letter-spacing:-1px;line-height:1}
.intro{position:absolute;left:20px;right:20px;top:200px;text-align:center;font-size:18px;line-height:23px;color:var(--ink);font-weight:400}
.feature{position:absolute;left:0;right:0}
.feature__title{display:flex;align-items:center;gap:8px;font-weight:700;font-size:21px;color:var(--green)}
.feature__body{font-style:italic;font-weight:300;font-size:17.5px;line-height:23px;color:var(--text-light);margin-top:4px}
.feature--clients{top:352px}
.feature--clients .feature__title{padding-left:18px}
.feature--clients .feature__body{padding-left:46px}
.feature--candidates{top:506px}
.feature--candidates .feature__title{padding-left:10px}
.feature--candidates .feature__body{padding-left:37px}
.chevron{width:18px;height:22px;flex:none}
.footer-bar{position:absolute;left:0;bottom:0;width:100%;height:55px;background:var(--green);display:flex}
.footer-bar__url{flex:1;display:flex;align-items:center;padding-left:25px;color:#fff;font-size:17px}
.footer-bar__accent{width:93px;background:var(--green-deep)}
.points{position:absolute;left:0;right:0;top:245px;list-style:none}
.point{display:flex;gap:22px;padding-left:31px;margin-bottom:22px}
.point .chevron{margin-top:3px}
.point__text{font-style:italic;font-weight:300;font-size:17.5px;line-height:23px;color:var(--text-light);width:270px}
.texture-band{position:absolute;left:0;top:505px;width:100%;height:48px;background:var(--pattern)}
.search-art{position:absolute;left:233px;top:414px;width:112px;height:112px;border-radius:50%;background:radial-gradient(circle at 45% 40%,#4a4b49,#2a2b29 70%);border:5px solid #bdbdbd}
.contact{position:absolute;left:0;bottom:0;width:100%;height:195px;background:var(--green);padding:14px 0 0 15px;color:#fff;font-size:14px;line-height:22.5px}
.contact__role{margin-bottom:1px}
.contact dt{font-weight:700;display:inline}
.contact dd{display:inline}
.contact__web{font-weight:700}
</style>
</head>
<body>

<section class="flyer flyer--front">
  <header class="header">
    <div class="brand"><span class="brand__dot"></span><span class="brand__name">NU Staffing</span></div>
    <p class="intro">With extensive years of recruitment experience we are the highest referred recruitment company in the Brisbane market.</p>
  </header>

  <article class="feature feature--clients">
    <h2 class="feature__title"><svg class="chevron" viewBox="0 0 18 22"><polyline points="3,2 15,11 3,20" fill="none" stroke="currentColor" stroke-width="3.5"/></svg>Why clients use NU</h2>
    <p class="feature__body">Our clients benefit from our<br>wealth of experience and knowl-<br>edge within their industry to<br>recruit the right candidate.</p>
  </article>

  <article class="feature feature--candidates">
    <h2 class="feature__title"><svg class="chevron" viewBox="0 0 18 22"><polyline points="3,2 15,11 3,20" fill="none" stroke="currentColor" stroke-width="3.5"/></svg>Why Candidates use NU</h2>
    <p class="feature__body">With our long standing experi-<br>ence within recruitment , we take<br>the time and care attitude to find<br>the right position and culture suit<br>your working experience</p>
  </article>

  <footer class="footer-bar">
    <span class="footer-bar__url">www.nustaffing-example.com.au</span>
    <span class="footer-bar__accent"></span>
  </footer>
</section>

<section class="flyer flyer--back">
  <header class="header">
    <div class="brand"><span class="brand__dot"></span><span class="brand__name">NU Staffing</span></div>
  </header>

  <ul class="points">
    <li class="point"><svg class="chevron" viewBox="0 0 18 22" style="color:var(--green)"><polyline points="3,2 15,11 3,20" fill="none" stroke="currentColor" stroke-width="3.5"/></svg><span class="point__text">Why Nu does quality and back-<br>ground checks on candidates</span></li>
    <li class="point"><svg class="chevron" viewBox="0 0 18 22" style="color:var(--green)"><polyline points="3,2 15,11 3,20" fill="none" stroke="currentColor" stroke-width="3.5"/></svg><span class="point__text">The advantage of using Nu<br>Staffing vs Recruitment<br>on your own</span></li>
    <li class="point"><svg class="chevron" viewBox="0 0 18 22" style="color:var(--green)"><polyline points="3,2 15,11 3,20" fill="none" stroke="currentColor" stroke-width="3.5"/></svg><span class="point__text">12 week Guarantee<br>period on all<br>placements</span></li>
  </ul>

  <div class="texture-band" role="img" aria-label="Subtle geometric texture band"></div>
  <div class="search-art" role="img" aria-label="Magnifying glass over a green running figure"></div>

  <address class="contact" style="font-style:normal">
    <div>Martin Holroyd</div>
    <div class="contact__role">Recruitment Manager</div>
    <dl>
      <div><dt>Mobile:</dt> <dd>0412 586 230</dd></div>
      <div><dt>Phone:</dt> <dd>3951 2407</dd></div>
      <div><dt>Fax:</dt> <dd>3951 2409</dd></div>
      <div><dt>E-mail:</dt> <dd>martin@nustaffing-example.com.au</dd></div>
    </dl>
    <div class="contact__web">www.nustaffing-example.com.au</div>
    <div>Level 1/ 218 Wexcombe Street, Spring Hill QLD 4004</div>
  </address>
</section>

</body>
</html>
```